New Design for our Velintor Gran Reserva Brandy, it is the label design for the bottle label

We need a new bottle label for our Brandy Gran Reserva that we want to bring to the market.

Please have a look at all our current bottles and labels and the feel of our company under www.velintor-example.ch

The bottle that we will be using for the brand is a different one than the one that we already have, the design of the bottle is attached with a document.

I have also attached a briefing in regards to Brandy in general for your information.

### 1. What is Brandy?
Brandy is a distilled spirit made from fermented wine or other fruit wines. It is traditionally aged in oak barrels, which gives it its characteristic color and rich flavor. The aging process in oak is essential for developing the aromas and quality of the brandy.

### 2. What is Brandy Reserva?
A Brandy labeled as "Reserva" has undergone a longer aging process, typically at least 2 to 3 years, in oak barrels. This aging gives the brandy a deeper, more complex flavor profile and a darker color. "Reserva" is often an indication of higher quality.

### 3. Who enjoys drinking Brandy?
Brandy is typically favored by those who appreciate a deep, rich tasting experience. This often includes older consumers who value the time-aged complexity of the spirit. However, Brandy is also gaining popularity among younger people, especially through cocktails and modern serving styles.

### 4. Why is Brandy trending?
Brandy is experiencing a resurgence as consumers increasingly value quality and artisanal production methods. Its versatility in cocktails and association with traditional, luxurious experiences have also contributed to its renewed popularity.

### 5. What colors would be associated with Brandy?
The typical colors associated with Brandy are warm gold, amber, and deep golden-brown tones. These colors reflect the aging process in oak barrels and the richness of the flavors. Other associated colors might include dark brown and mahogany.

### 6. What is important to customers when buying Brandy?
Customers care about the origin of the Brandy, the aging time, the quality of the ingredients, the production method, and the brand. They also pay attention to the prestige of the product and the authenticity of the production.

### 7. What is not important to customers when buying Brandy?
For many customers, the price and packaging (unless it’s especially exclusive) may be less important than the quality and taste of the Brandy. The distillery name might be less significant if it isn’t tied to a particular reputation.

### 8. What do customers know about Swiss Brandy?
Swiss Brandy is still relatively unknown in many markets, but customers who are familiar with it appreciate the precision and quality of Swiss production. Swiss Brandy is assumed to be made with care and under strict quality standards.

### 9. What is Brandy Gran Reserva?
**Brandy Gran Reserva** is an even higher quality and longer-aged version of Brandy. Generally, a Gran Reserva is aged for at least 5 to 10 years or more in oak barrels. This extended aging process gives the Brandy an especially deep, complex flavor profile and often a darker, richer color. Gran Reserva is often regarded as the top-tier product within a Brandy range and appeals to discerning consumers who value quality, refinement, and a luxurious tasting experience.

The label “Gran Reserva” thus indicates the highest quality level for Brandies, similar to other spirits (like wine or whisky), where the aging time is a critical factor.

### 10. What emotions are associated with Brandy?
Brandy is often associated with luxury, relaxation, and comfort. It evokes feelings of tradition, elegance, and sophistication. Drinking Brandy is frequently seen as a moment of reflection and enjoyment.

### 11. How should Brandy be marketed?
Brandy should be marketed with a focus on its artisanal production, quality, and tradition. A narrative around the product, its aging, and origin can help create an emotional connection with the customer. The marketing should also emphasize the versatility of Brandy, whether consumed neat or in cocktails.

### 12. Sales test and label design for Velintor Brandy
For a sales test, I would suggest a tasting in an upscale setting, perhaps paired with a storytelling presentation highlighting the history of the 6-year aged Brandy and its aging in oak barrels.

**Label design**:
The label should reflect the exclusivity of the product, with an elegant, minimalist design. Colors like deep gold, mahogany, and a hint of deep blue could be used to emphasize the aging and quality of the Brandy. The label should include information about the aging time, the use of oak barrels, and a brief story about the Brandy’s production. A seal or embossing highlighting the craftsmanship would also be fitting.

Target Market(s)

Customers that like Brandy

Requirements
Must have
• the Alcohol % must be included on the label as well as our address.

```html
<!DOCTYPE html>
<html lang="en">
<head>
<meta charset="utf-8">
<title>Velintor Brandy Grand Reserva – Label Variants</title>
<link rel="stylesheet" href="https://fonts.googleapis.com/css2?family=Bebas+Neue&family=Cormorant+Garamond:wght@400;500&family=Libre+Baskerville:wght@400;700&family=Montserrat:wght@400&family=Pinyon+Script&display=swap">
<style>
  :root {
    --backdrop: #e6e7e9;
    --navy: #0e1c30;
    --gold: #c9961f;
    --ink-light: #ffffff;
    --ink-soft: #e9e6df;
  }
  * { margin: 0; padding: 0; box-sizing: border-box; }
  html, body { width: 829px; height: 1200px; overflow: hidden; background: var(--backdrop); }
  .sheet { position: relative; width: 829px; height: 1200px; }

  .label { position: absolute; width: 290px; height: 582px; color: var(--ink-light); }
  .label--bold { left: 102px; top: 12px; }
  .label--fine { left: 437px; top: 12px; }
  .label--swash { left: 269px; top: 606px; }

  .label__shape { position: absolute; inset: 0; width: 290px; height: 582px; }
  .label__text { position: absolute; left: 0; width: 100%; text-align: center; }

  .brand { top: 158px; font-family: "Libre Baskerville", serif; font-weight: 700; font-size: 15px; letter-spacing: 0.5px; }
  .brand-sub { top: 178px; font-family: "Libre Baskerville", serif; font-weight: 700; font-size: 5.5px; line-height: 1.25; letter-spacing: 0.6px; }

  .title-bold { top: 232px; font-family: "Bebas Neue", sans-serif; font-weight: 400; font-size: 92px; line-height: 1; letter-spacing: 1px; }
  .subtitle-bold { top: 318px; font-family: "Libre Baskerville", serif; font-size: 11.5px; letter-spacing: 1.6px; }

  .title-fine { top: 262px; font-family: "Cormorant Garamond", serif; font-weight: 400; font-size: 36px; line-height: 1; letter-spacing: 1.5px; }
  .subtitle-fine { top: 299px; font-family: "Montserrat", sans-serif; font-size: 6.5px; letter-spacing: 1.8px; }

  .title-swash { top: 246px; display: flex; justify-content: center; align-items: flex-start; font-family: "Cormorant Garamond", serif; font-weight: 400; }
  .title-swash__initial { font-size: 66px; line-height: 1; }
  .title-swash__rest { display: flex; flex-direction: column; align-items: flex-start; padding-top: 9px; }
  .title-swash__word { font-size: 40px; line-height: 1; letter-spacing: 1px; }
  .title-swash__sub { margin-top: 2px; margin-left: -8px; font-family: "Montserrat", sans-serif; font-size: 6.5px; line-height: 1; letter-spacing: 1.6px; }

  .variety { top: 396px; font-family: "Pinyon Script", cursive; font-size: 29px; line-height: 1; }
  .strength { top: 450px; font-family: "Libre Baskerville", serif; font-size: 11px; letter-spacing: 1.4px; }
  .story { top: 472px; left: 76px; width: 138px; font-family: "Libre Baskerville", serif; font-size: 5px; line-height: 1.6; color: var(--ink-soft); }

  .volume-row { top: 517px; left: 52px; width: 190px; height: 12px; display: flex; justify-content: space-between; align-items: center; font-family: "Libre Baskerville", serif; font-size: 7px; }
  .abv small { font-size: 3.5px; display: inline-block; line-height: 1.1; vertical-align: 2px; text-align: left; }
</style>
</head>
<body>
<main class="sheet">

  <article class="label label--bold">
    <svg class="label__shape" viewBox="0 0 290 582" aria-hidden="true">
      <polygon fill="var(--navy)" points="145,0 290,120 290,148 145,30 0,148 0,120"/>
      <polygon fill="var(--navy)" points="145,50 290,168 290,582 0,582 0,168"/>
      <polygon fill="none" stroke="var(--gold)" stroke-width="2.5" points="145,100 250,178 250,543 40,543 40,178"/>
      <line x1="62" y1="208" x2="228" y2="208" stroke="var(--gold)" stroke-width="1.5"/>
      <line x1="62" y1="368" x2="228" y2="368" stroke="var(--gold)" stroke-width="1.5"/>
      <line x1="88" y1="377" x2="202" y2="377" stroke="var(--gold)" stroke-width="1.5"/>
      <line x1="96" y1="523" x2="195" y2="523" stroke="var(--gold)" stroke-width="1.5"/>
    </svg>
    <div role="img" aria-label="Faint botanical line pattern across the label ground"></div>
    <p class="label__text brand">Velintor</p>
    <p class="label__text brand-sub">SWISS<br>DISTILLERY</p>
    <h1 class="label__text title-bold">BRANDY</h1>
    <p class="label__text subtitle-bold">GRAND RESERVA</p>
    <p class="label__text variety">Single Malt</p>
    <p class="label__text strength">CASK STRENGTH</p>
    <p class="label__text story">Lorem ipsum dolor sit amet, consectetur adipiscing elit, sed do eiusmod tempor incididunt ut labore et dolore magna aliqua</p>
    <div class="label__text volume-row"><span class="abv">40% <small>ALC.<br>/VOL.</small></span><span>750 ML</span></div>
  </article>

  <article class="label label--fine">
    <svg class="label__shape" viewBox="0 0 290 582" aria-hidden="true">
      <polygon fill="var(--navy)" points="145,0 290,120 290,148 145,30 0,148 0,120"/>
      <polygon fill="var(--navy)" points="145,50 290,168 290,582 0,582 0,168"/>
      <polygon fill="none" stroke="var(--gold)" stroke-width="2.5" points="145,100 250,178 250,543 40,543 40,178"/>
      <line x1="62" y1="208" x2="228" y2="208" stroke="var(--gold)" stroke-width="1.5"/>
      <line x1="62" y1="368" x2="228" y2="368" stroke="var(--gold)" stroke-width="1.5"/>
      <line x1="88" y1="377" x2="202" y2="377" stroke="var(--gold)" stroke-width="1.5"/>
      <line x1="96" y1="523" x2="195" y2="523" stroke="var(--gold)" stroke-width="1.5"/>
    </svg>
    <div role="img" aria-label="Faint botanical line pattern across the label ground"></div>
    <p class="label__text brand">Velintor</p>
    <p class="label__text brand-sub">SWISS<br>DISTILLERY</p>
    <h2 class="label__text title-fine">BRANDY</h2>
    <p class="label__text subtitle-fine">GRAND RESERVA</p>
    <p class="label__text variety">Single Malt</p>
    <p class="label__text strength">CASK STRENGTH</p>
    <p class="label__text story">Lorem ipsum dolor sit amet, consectetur adipiscing elit, sed do eiusmod tempor incididunt ut labore et dolore magna aliqua</p>
    <div class="label__text volume-row"><span class="abv">40% <small>ALC.<br>/VOL.</small></span><span>750 ML</span></div>
  </article>

  <article class="label label--swash">
    <svg class="label__shape" viewBox="0 0 290 582" aria-hidden="true">
      <polygon fill="var(--navy)" points="145,0 290,120 290,148 145,30 0,148 0,120"/>
      <polygon fill="var(--navy)" points="145,50 290,168 290,582 0,582 0,168"/>
      <polygon fill="none" stroke="var(--gold)" stroke-width="2.5" points="145,100 250,178 250,543 40,543 40,178"/>
      <line x1="62" y1="208" x2="228" y2="208" stroke="var(--gold)" stroke-width="1.5"/>
      <line x1="62" y1="368" x2="228" y2="368" stroke="var(--gold)" stroke-width="1.5"/>
      <line x1="88" y1="377" x2="202" y2="377" stroke="var(--gold)" stroke-width="1.5"/>
      <line x1="96" y1="523" x2="195" y2="523" stroke="var(--gold)" stroke-width="1.5"/>
    </svg>
    <div role="img" aria-label="Faint botanical line pattern across the label ground"></div>
    <p class="label__text brand">Velintor</p>
    <p class="label__text brand-sub">SWISS<br>DISTILLERY</p>
    <h2 class="label__text title-swash">
      <span class="title-swash__initial">B</span>
      <span class="title-swash__rest">
        <span class="title-swash__word">RANDY</span>
        <span class="title-swash__sub">GRAND RESERVA</span>
      </span>
    </h2>
    <p class="label__text variety">Single Malt</p>
    <p class="label__text strength">CASK STRENGTH</p>
    <p class="label__text story">Lorem ipsum dolor sit amet, consectetur adipiscing elit, sed do eiusmod tempor incididunt ut labore et dolore magna aliqua</p>
    <div class="label__text volume-row"><span class="abv">40% <small>ALC.<br>/VOL.</small></span><span>750 ML</span></div>
  </article>

</main>
</body>
</html>
```